My website design

It Will be a to-go website for all service requests from the comfort of your home. services ranging from renting an electrician to fix your home electrical issues, DJ for your party, mark-up artist for your wedding and so on. Here are a few websites for inspiration:

https://www.dwellpanel.example/
https://www.chorewren.example/
https://www.gigplover.example/

Number of Pages Required

5+ page

Requirements
Must have
• User's registration form
pros resgistation form
filling out job request form
quotes sent sent back to job requester from various pros within the same zip code
quote accepted
ability to review pros once jobs are completed

```html
<!DOCTYPE html>
<html lang="en">
<head>
<meta charset="utf-8">
<title>Tradevo – Sign Up</title>
<link rel="stylesheet" href="https://fonts.googleapis.com/css2?family=Poppins:wght@400;500;600&display=swap">
<style>
  :root {
    --green: #3bb54a;
    --white: #ffffff;
    --ink: #111111;
    --label: #1c1c1c;
    --placeholder: #6b6b6b;
    --field-border: #b9b9b9;
    --hero-dark: #4d5c68;
    --hero-mid: #6c7a85;
    --hero-warm: #7d6a6a;
    --hero-olive: #7c7f5e;
  }
  * { box-sizing: border-box; margin: 0; padding: 0; }
  html, body {
    width: 1200px; height: 588px; overflow: hidden;
    font-family: "Poppins", sans-serif;
  }
  .page { position: relative; width: 1200px; height: 588px; overflow: hidden; }
  .hero-photo {
    position: absolute; inset: 0;
    background:
      radial-gradient(ellipse 260px 200px at 200px 260px, var(--hero-warm), transparent 70%),
      radial-gradient(ellipse 240px 260px at 1000px 360px, var(--hero-olive), transparent 70%),
      radial-gradient(ellipse 420px 360px at 600px 380px, var(--hero-dark), transparent 75%),
      linear-gradient(180deg, #7a8690 0%, var(--hero-mid) 50%, #66737d 100%);
  }
  .site-header { position: absolute; inset: 0 0 auto 0; height: 90px; }
  .brand {
    position: absolute; left: 86px; top: 30px;
    display: flex; align-items: center; gap: 10px;
    color: var(--white); text-decoration: none;
    font-size: 22px; font-weight: 500; letter-spacing: 8px;
  }
  .brand-mark { width: 26px; height: 26px; background: var(--green); }
  .join-pro {
    position: absolute; left: 784px; top: 31px; width: 125px; height: 39px;
    background: var(--green); color: var(--white);
    font-size: 11.5px; font-weight: 600;
    display: flex; align-items: center; justify-content: center;
    text-decoration: none;
  }
  .nav-link {
    position: absolute; top: 40px; color: var(--white);
    font-size: 12px; font-weight: 500; text-decoration: none;
  }
  .nav-explore { left: 942px; }
  .nav-signup { left: 1013px; }
  .nav-login { left: 1084px; }
  .signup-card {
    position: absolute; left: 434px; top: 102px; width: 331px; height: 446px;
    background: var(--white); border-radius: 5px;
  }
  .signup-title {
    position: absolute; left: 0; right: 0; top: 18px; text-align: center;
    font-size: 25px; font-weight: 500; color: var(--ink);
  }
  .field-label {
    position: absolute; left: 25px; font-size: 11px; color: var(--label);
  }
  .field {
    position: absolute; left: 25px; width: 283px; height: 45px;
    border: 1px solid var(--field-border); border-radius: 2px;
    padding: 0 17px; font-family: inherit; font-size: 11px; color: var(--ink);
    background: var(--white);
  }
  .field::placeholder { color: var(--placeholder); }
  .toggle-visibility { position: absolute; left: 278px; top: 240px; width: 14px; height: 10px; }
  .create-account {
    position: absolute; left: 25px; top: 382px; width: 283px; height: 45px;
    border: none; border-radius: 2px; background: var(--green); color: var(--white);
    font-family: inherit; font-size: 14px;
  }
</style>
</head>
<body>
<div class="page">
  <div class="hero-photo" role="img" aria-label="Blurred photo of a tradesman wearing a plaid shirt and tool belt, holding a power drill and a coiled yellow cable, under a grey-blue overlay"></div>

  <header class="site-header">
    <a class="brand" href="#"><span class="brand-mark"></span>TRADEVO</a>
    <a class="join-pro" href="#">Join as a pro</a>
    <a class="nav-link nav-explore" href="#">Explore</a>
    <a class="nav-link nav-signup" href="#">Sign Up</a>
    <a class="nav-link nav-login" href="#">Log in</a>
  </header>

  <form class="signup-card">
    <h1 class="signup-title">Sign Up</h1>

    <label class="field-label" style="top:61px" for="name">Name</label>
    <input class="field" style="top:85px" id="name" type="text" placeholder="ex: Johnsmith">

    <label class="field-label" style="top:143px" for="email">Email Address</label>
    <input class="field" style="top:168px" id="email" type="email" placeholder="demo@mailbox.example">

    <label class="field-label" style="top:222px" for="password">Password</label>
    <input class="field" style="top:247px" id="password" type="password" value="*********">
    <svg class="toggle-visibility" viewBox="0 0 14 10" aria-hidden="true">
      <path d="M1 5 C4 0.5 10 0.5 13 5 C10 9.5 4 9.5 1 5 Z" fill="none" stroke="#8a8a8a" stroke-width="1.1"/>
      <circle cx="7" cy="5" r="2" fill="#8a8a8a"/>
    </svg>

    <label class="field-label" style="top:300px" for="zip">Zip Code</label>
    <input class="field" style="top:325px" id="zip" type="text">

    <button class="create-account" type="submit">Create Account</button>
  </form>
</div>
</body>
</html>
```